bluegum voyages

We provide boar charter for :Fishing/whale watching and diving in Sydney Harbour providing for 12 passengersI have yet to have web page made but want to make logo first then do web page later. So I want to be able to edit and add this site to card later

Contact Information for Business Card

Captain Art (Doc) Wigellphone no 0457710098email awigell4@gmail.comCompany name Marlow Outings Pty Ltd in association with far reef cruises

Font styles to use
Serif

Requirements
Nice to have
• perhaps a photo of boat and some stick diagrams of fishing.whales and diviving

```html
<!DOCTYPE html>
<html lang="en">
<head>
<meta charset="utf-8">
<title>Marlow Outings Pty Ltd – Business Card</title>
<link href="https://fonts.googleapis.com/css2?family=Montserrat:wght@400;600;700&display=swap" rel="stylesheet">
<style>
  :root {
    --bg: #2b2b2d;
    --navy: #2b3190;
    --sun: #f7e21b;
    --white: #ffffff;
    --sky: #9fc8ea;
    --water: #3f6f95;
    --sketch: #dfe3f2;
  }
  * { margin: 0; padding: 0; box-sizing: border-box; }
  html, body { width: 1200px; height: 659px; overflow: hidden; }
  body {
    background: var(--bg);
    font-family: "Montserrat", sans-serif;
    position: relative;
  }
  .card {
    position: absolute;
    top: 181px;
    width: 520px;
    height: 297px;
    background: var(--white);
    overflow: hidden;
    box-shadow: 0 10px 28px rgba(0,0,0,.45);
  }
  .card--front { left: 60px; }
  .card--back { left: 620px; }
  .card svg.card__art { position: absolute; inset: 0; width: 100%; height: 100%; }

  .brand {
    position: absolute;
    display: flex;
    align-items: center;
    gap: 10px;
  }
  .brand__dot {
    width: 34px; height: 34px; border-radius: 50%;
    background: var(--sun);
    flex: none;
  }
  .brand__name {
    font-weight: 700;
    font-size: 21px;
    color: var(--navy);
    white-space: nowrap;
  }
  .card--front .brand { left: 34px; top: 236px; }
  .card--back .brand { left: 30px; top: 118px; }

  .sketch {
    position: absolute;
    left: 366px; top: 24px;
    width: 70px; height: 62px;
    background: var(--sketch);
    border-radius: 4px;
  }

  .contact {
    position: absolute;
    right: 26px;
    top: 112px;
    text-align: right;
    color: var(--white);
  }
  .contact__name { font-weight: 700; font-size: 17px; }
  .contact__alias { color: var(--sun); font-size: 9px; margin-top: 1px; }
  .contact__line {
    display: flex; justify-content: flex-end; align-items: center; gap: 8px;
    font-size: 10px; margin-top: 10px;
  }
  .contact__line:first-of-type { margin-top: 22px; }
  .contact__line svg { width: 12px; height: 12px; flex: none; }
</style>
</head>
<body>

<section class="card card--front">
  <svg class="card__art" viewBox="0 0 520 297" preserveAspectRatio="none">
    <defs>
      <linearGradient id="harbourTone" x1="0" y1="0" x2="0" y2="1">
        <stop offset="0" stop-color="var(--sky)"/>
        <stop offset="1" stop-color="var(--water)"/>
      </linearGradient>
    </defs>
    <path role="img" aria-label="Photo of the charter boat cruising on Sydney Harbour"
          d="M0,0 H520 V60 C400,150 250,200 0,215 Z" fill="url(#harbourTone)"/>
    <path class="wave-band" d="M0,215 C250,200 400,150 520,60 V74 C420,170 260,226 0,246 Z" fill="var(--navy)"/>
  </svg>
  <div class="brand">
    <span class="brand__dot"></span>
    <span class="brand__name">Marlow Outings Pty Ltd</span>
  </div>
</section>

<section class="card card--back">
  <svg class="card__art" viewBox="0 0 520 297" preserveAspectRatio="none">
    <path class="wave-accent" d="M0,268 C150,266 290,228 368,138 C420,78 470,52 520,42 V60 C480,70 432,92 382,150 C302,242 152,282 0,284 Z" fill="var(--sun)"/>
    <path class="wave-panel" d="M0,297 V284 C152,282 302,242 382,150 C432,92 480,70 520,60 V297 Z" fill="var(--navy)"/>
  </svg>
  <div class="sketch" role="img" aria-label="Stick drawing of a diver holding a fishing rod with small fish"></div>
  <div class="brand">
    <span class="brand__dot"></span>
    <span class="brand__name">Marlow Outings Pty Ltd</span>
  </div>
  <div class="contact">
    <div class="contact__name">Captain Len</div>
    <div class="contact__alias">Skip</div>
    <div class="contact__line">
      <span>0468231594</span>
      <svg viewBox="0 0 24 24"><path fill="var(--sun)" d="M6.6 10.8a15 15 0 0 0 6.6 6.6l2.2-2.2a1 1 0 0 1 1-.25 11.4 11.4 0 0 0 3.6.57 1 1 0 0 1 1 1V20a1 1 0 0 1-1 1A17 17 0 0 1 3 4a1 1 0 0 1 1-1h3.5a1 1 0 0 1 1 1c0 1.25.2 2.45.57 3.6a1 1 0 0 1-.25 1z"/></svg>
    </div>
    <div class="contact__line">
      <span>email lpruntel7@tidewake.net</span>
      <svg viewBox="0 0 24 24"><rect x="2" y="5" width="20" height="14" rx="1.5" fill="none" stroke="var(--sun)" stroke-width="2"/><path d="M3 6l9 7 9-7" fill="none" stroke="var(--sun)" stroke-width="2"/></svg>
    </div>
  </div>
</section>

</body>
</html>
```